Business Cards that are elegant and wow

I want to create and print business cards that represent my brand and stand out from the rest. We want to ensure they stay in our branding and the integrity is not lost. I am happy to look at different shapes like square etc.

It will be printed on very thick cards and will be stylish .

I want to create and print business cards that represent my brand and stand out from the rest. We want to ensure they stay in ur branding and the integrity is not lost. I am happy to look at different shapes like square etc.

Target Market(s)

real estate professionals

Industry/Entity Type

Real Estate

Contact Information for Business Card

Maren Holt
hello@brightfernrealty.com.au
brightfernrealty.com.au
0487 316 252 (SMS)

Colors

Designer to choose colors to be used in the design.

Requirements
Must have
• My logo
• email
• website
• Name
Nice to have
• I like the idea of printing with foil or spot gloss. You want it to stand out in a sea.
Should not have
• I would like you to stay in my colour themes. Don't change the colour of my logo

```html
<!DOCTYPE html>
<html lang="en">
<head>
<meta charset="utf-8">
<title>Bright Fern – Business Card, Front and Back</title>
<link rel="stylesheet" href="https://fonts.googleapis.com/css2?family=EB+Garamond:ital,wght@0,500;0,600;1,400&family=Montserrat:wght@500&display=swap">
<style>
  :root {
    --page: #ffffff;
    --sky-top: #ffffff;
    --sky-mid: #29abe2;
    --sky-deep: #2b3a8f;
    --navy: #272060;
    --card-edge: #2a2a3a;
    --city-top: #ec008c;
    --city-bottom: #9b1560;
    --band-1: #cc2270;
    --band-2: #e61f73;
    --band-3: #ff2a8a;
    --band-4: #fb7ec6;
    --band-5: #f5aedb;
    --logo-blue: #29abe2;
    --text-light: #ffffff;
  }
  * { margin: 0; padding: 0; box-sizing: border-box; }
  html, body {
    width: 1200px; height: 1200px; overflow: hidden;
    background: var(--page);
  }
  .canvas { position: relative; width: 1200px; height: 1200px; }

  .card { position: absolute; overflow: hidden; }

  .card--front {
    left: 238px; top: 348px; width: 327px; height: 504px;
    border: 1.5px solid var(--card-edge);
    background: linear-gradient(180deg,
      var(--sky-top) 0%, var(--sky-mid) 24%, #2488cf 52%, var(--sky-deep) 72%, var(--sky-deep) 100%);
  }
  .card--back {
    left: 654px; top: 345px; width: 325px; height: 508px;
    background: var(--navy);
  }

  .swatch-stack { position: absolute; display: flex; flex-direction: column; }
  .swatch-stack span { display: block; height: 33.2px; }
  .swatch-stack span:nth-child(1) { background: var(--band-1); }
  .swatch-stack span:nth-child(2) { background: var(--band-2); }
  .swatch-stack span:nth-child(3) { background: var(--band-3); }
  .swatch-stack span:nth-child(4) { background: var(--band-4); }
  .swatch-stack span:nth-child(5) { background: var(--band-5); }

  .card--front .swatch-stack--left  { left: -1px; top: 114px; width: 62px; }
  .card--front .swatch-stack--right { left: 259px; top: 114px; width: 67px; }
  .card--back .swatch-stack--left   { left: 0; top: 121px; width: 65px; }
  .card--back .swatch-stack--right  { left: 260px; top: 121px; width: 65px; }

  .brand-block { position: absolute; left: 74px; top: 113px; color: var(--text-light); font-family: "EB Garamond", serif; }
  .brand-name { font-size: 21px; font-weight: 500; letter-spacing: 0.3px; line-height: 1; }
  .brand-tagline { font-size: 11.5px; font-style: italic; margin-top: 3px; }

  .contact-block { position: absolute; left: 74px; top: 198px; color: var(--text-light); font-family: "EB Garamond", serif; }
  .contact-name { font-size: 16px; font-weight: 600; margin-bottom: 6px; }
  .contact-line { font-size: 11px; font-style: italic; line-height: 21.5px; }

  .skyline {
    position: absolute; left: 0; bottom: 0; width: 100%; height: 170px;
    background: linear-gradient(180deg, var(--city-top) 0%, var(--city-bottom) 100%);
  }

  .back-logo {
    position: absolute; left: 162px; top: 340px;
    display: flex; align-items: center; gap: 14px;
    transform: translate(-50%, -50%) rotate(-90deg);
    white-space: nowrap;
  }
  .back-logo__dot {
    width: 46px; height: 46px; border-radius: 50%;
    border: 3px solid var(--logo-blue);
  }
  .back-logo__name {
    font-family: "EB Garamond", serif; font-weight: 500;
    font-size: 38px; letter-spacing: 1px; color: var(--logo-blue);
  }
</style>
</head>
<body>
<main class="canvas">
  <section class="card card--front" aria-label="Business card front">
    <div class="swatch-stack swatch-stack--left"><span></span><span></span><span></span><span></span><span></span></div>
    <div class="swatch-stack swatch-stack--right"><span></span><span></span><span></span><span></span><span></span></div>

    <div class="brand-block">
      <div class="brand-name">BRIGHT FERN</div>
      <div class="brand-tagline">real estate professionals</div>
    </div>

    <div class="contact-block">
      <div class="contact-name">Maren Holt</div>
      <div class="contact-line">hello@brightfernrealty.com.au</div>
      <div class="contact-line">brightfernrealty.com.au</div>
      <div class="contact-line">0487 316 252 (SMS)</div>
    </div>

    <div class="skyline" role="img" aria-label="Pink city skyline of tall buildings and a spire"></div>
  </section>

  <section class="card card--back" aria-label="Business card back">
    <div class="swatch-stack swatch-stack--left"><span></span><span></span><span></span><span></span><span></span></div>
    <div class="swatch-stack swatch-stack--right"><span></span><span></span><span></span><span></span><span></span></div>

    <div class="back-logo">
      <span class="back-logo__dot"></span>
      <span class="back-logo__name">BRIGHT FERN</span>
    </div>
  </section>
</main>
</body>
</html>
```